Real Estate Wordpress Landing Page

I'm looking to a landing page dedicated to my real estate brokerage that's catered to promoting that my company provides 1.5% listings to home sellers... I have a couple examples that I'm really looking towards mocking in a version with similar color schemes using my current company colors/website.

http://lorvanta.com/
https://www.bluthorn.com/about/one-percent-listing-fee

My brokerage company website is http://www.calmridge.us/

Target Market(s)

real estate home sellers & buyers

Industry/Entity Type

Real Estate

Coding

Coded - Design and coding required

Number of Pages Required

1 page

Colors
3176b5
0255a3
eaf1f7
cedeed

Requirements
Must have
• Company website colors - http://www.calmridge.us/
• Something around the lines of this website page - http://lorvanta.com/
• Wordpress compatibility

```html
<!DOCTYPE html>
<html lang="en">
<head>
<meta charset="utf-8">
<title>Calmridge Realty – 1.5% Listing Commission</title>
<link rel="stylesheet" href="https://fonts.googleapis.com/css2?family=Questrial&family=Open+Sans:ital,wght@0,400;0,600;0,700;1,700&display=swap">
<style>
:root{
  --blue:#3176b5;
  --blue-deep:#0255a3;
  --ice:#eaf1f7;
  --mist:#cedeed;
  --ink:#1d1d1f;
  --grey-text:#b3b3b3;
  --panel:#f2f2f2;
  --card:#f4f4f4;
  --bar:#2b2b2b;
}
*{box-sizing:border-box;margin:0;padding:0}
html,body{width:1200px;height:2528px;overflow:hidden;background:#fff}
body{position:relative;font-family:"Open Sans",Arial,sans-serif;color:var(--ink)}
.abs{position:absolute}
.heading{font-family:"Questrial","Century Gothic",sans-serif}

/* header */
.brand{left:162px;top:22px;display:flex;align-items:center;gap:10px}
.brand-mark{width:40px;height:40px;background:var(--blue)}
.brand-name{font-family:"Open Sans",sans-serif;font-weight:700;font-size:22px;color:var(--blue-deep)}
.phone{left:655px;top:38px;display:flex;align-items:center;gap:10px;color:var(--blue);font-size:15px;font-weight:600}
.btn{display:flex;align-items:center;justify-content:center;font-size:10px;font-weight:700;letter-spacing:.5px}
.btn-buy{left:795px;top:35px;width:118px;height:29px;background:var(--mist);color:var(--ink)}
.btn-sell{left:923px;top:35px;width:115px;height:29px;background:var(--blue);color:#fff}

/* hero */
.hero{left:0;top:101px;width:1200px;height:362px;background:linear-gradient(180deg,#2a4569 0%,#3a5676 55%,#44603e 85%,#55704c 100%)}
.hero::after{content:"";position:absolute;inset:0;background:rgba(18,42,82,.45)}
.hero-kicker{left:0;top:206px;width:1200px;text-align:center;color:#fff;font-size:19px;z-index:2}
.hero-title{left:263px;top:258px;width:674px;height:79px;border:2px solid #fff;display:flex;align-items:center;justify-content:center;color:#fff;font-size:54px;z-index:2}

/* intro */
.intro{left:0;top:463px;width:1200px;height:452px;background:var(--panel)}
.intro-logo{left:162px;top:559px;width:242px;height:252px;background:#e4e4e4;display:flex;align-items:center;justify-content:center;gap:8px}
.intro-logo .brand-mark{width:28px;height:28px}
.intro-logo .brand-name{font-size:22px}
.agent-name{left:431px;top:572px;width:245px;white-space:nowrap;font-size:27px;font-weight:700;color:var(--blue-deep);letter-spacing:.5px}
.intro-copy{left:431px;top:634px;width:245px;font-size:14px;line-height:20px;color:var(--grey-text);font-weight:600}
.amp{left:431px;top:676px;font-size:42px;font-weight:700;color:var(--blue)}
.intro-copy.more{top:732px}

/* form */
.lead-form{left:701px;top:396px;width:317px;height:415px;background:#fff;border:1px solid #e6e6e6;padding:16px 30px 0;z-index:3}
.lead-form h2{font-family:"Questrial",sans-serif;font-size:17px;color:#111;margin-bottom:16px;font-weight:700}
.field{height:37px;border:1px solid #e3e3e3;margin-bottom:10px;font-size:10px;color:#999;padding:12px 12px}
.field.area{height:81px;margin-bottom:20px}
.submit{height:40px;background:var(--blue);color:#fff;font-size:14px;font-style:italic;font-weight:700;display:flex;align-items:center;justify-content:center;letter-spacing:1px}
.form-shadow{left:730px;top:830px;width:260px;height:24px;border-radius:50%;background:radial-gradient(ellipse,rgba(0,0,0,.16),rgba(0,0,0,0) 70%)}

/* section headings with brackets */
.section-title{left:0;width:1200px;text-align:center;font-size:34px;font-weight:700;font-family:"Questrial",sans-serif}
.section-title span{color:var(--blue-deep)}
.bracket{border-top:2px solid var(--blue);height:38px}
.bracket.l{border-left:2px solid var(--blue)}
.bracket.r{border-right:2px solid var(--blue)}

/* latest property */
.feature-card{left:236px;top:1092px;width:334px;height:305px;background:var(--blue)}
.photo{background:linear-gradient(160deg,#9bc3e6 0%,#dcdcd6 45%,#c9c4b8 70%,#7a8f5e 100%)}
.feature-photo{left:266px;top:1122px;width:273px;height:175px}
.feature-addr{left:236px;top:1312px;width:334px;text-align:center;color:#fff;font-size:13px;font-weight:700}
.pill{height:27px;display:flex;align-items:center;justify-content:center;font-size:12px;font-weight:700;background:var(--ice);color:var(--ink)}
.feature-lead{left:620px;top:1142px;font-size:25px;font-weight:700;color:#222}
.feature-lead b{color:var(--blue-deep)}
.feature-sub{left:620px;top:1200px;width:360px;font-size:26px;line-height:33px;font-weight:700;color:#c4c4c4}
.arrow-btn{width:41px;height:41px;border:2px solid var(--blue-deep);display:flex;align-items:center;justify-content:center}
.arrow-btn.off{border:1px solid #ddd}

/* listing cards */
.listing{width:277px;height:396px;top:1602px;background:var(--card)}
.listing .photo{height:231px}
.listing .addr{position:absolute;left:15px;top:250px;font-size:11.5px;font-weight:700}
.listing .price{position:absolute;left:15px;top:268px;font-size:13px;font-weight:700;color:var(--blue)}
.listing ul{position:absolute;left:15px;top:295px;list-style:none;font-size:10.5px;line-height:17px;color:#777;font-weight:600}
.listing .call{position:absolute;left:15px;top:356px;width:106px;height:27px;background:var(--mist);font-size:12px;font-weight:700;display:flex;align-items:center;justify-content:center}
.listing .tel{position:absolute;left:125px;top:356px;width:138px;height:27px;background:var(--blue);color:#fff;font-size:12px;font-weight:700;display:flex;align-items:center;justify-content:center}

/* broker band */
.band{left:0;top:2111px;width:1200px;height:282px;background:linear-gradient(180deg,#f4f4f4,#ebebeb)}
.band-title{left:0;top:2168px;width:1200px;text-align:center;font-size:34px;font-weight:700;font-family:"Questrial",sans-serif}
.band-copy{left:0;top:2226px;width:1200px;text-align:center;font-size:15px;line-height:22px;color:#666}
.band-btn{left:426px;top:2292px;width:347px;height:38px;background:var(--blue);color:#fff;font-size:15px;font-weight:700;font-style:italic;display:flex;align-items:center;justify-content:center}

/* footer */
.foot-note{left:0;top:2425px;width:1200px;text-align:center;font-size:15px;line-height:22px;color:#999}
.foot-note b{color:var(--blue-deep);font-weight:700}
.copyright{left:0;top:2497px;width:1200px;height:31px;background:var(--bar);color:#999;font-size:9px;display:flex;align-items:center;justify-content:center}
</style>
</head>
<body>

<header>
  <div class="abs brand"><span class="brand-mark"></span><span class="brand-name">Calmridge</span></div>
  <div class="abs phone">
    <svg width="10" height="16" viewBox="0 0 10 16"><path d="M8 1 C3 3 2 13 8 15" fill="none" stroke="#3176b5" stroke-width="2.4" stroke-linecap="round"/></svg>
    555-204-7730
  </div>
  <div class="abs btn btn-buy">BUY WITH US</div>
  <div class="abs btn btn-sell">SELL WITH US</div>
</header>

<section>
  <div class="abs hero" role="img" aria-label="Photo of a two-storey tiled-roof house on a sunny suburban street"></div>
  <p class="abs hero-kicker heading">GET FULL SERVICE FOR</p>
  <h1 class="abs hero-title heading">1.5% Listing Commission</h1>
</section>

<section>
  <div class="abs intro"></div>
  <div class="abs intro-logo"><span class="brand-mark"></span><span class="brand-name">Calmridge</span></div>
  <h2 class="abs agent-name">/ NOEL DARVEN</h2>
  <p class="abs intro-copy">On average, our customers save $5,600 when they list with us</p>
  <div class="abs amp">&amp;</div>
  <p class="abs intro-copy more">they still receive top marketing and quality professional service!<br>CALL US TODAY AND SAVE THOUSANDS $$$</p>

  <form class="abs lead-form">
    <h2>Talk to a Local Calmridge Agent</h2>
    <div class="field">First Name and Last Name*</div>
    <div class="field">Email*</div>
    <div class="field">Tel*</div>
    <div class="field">Select*</div>
    <div class="field area">Comment</div>
    <div class="submit">SUBMIT</div>
  </form>
  <div class="abs form-shadow"></div>
</section>

<section>
  <div class="abs bracket l" style="left:162px;top:1011px;width:138px"></div>
  <div class="abs bracket r" style="left:901px;top:1011px;width:137px"></div>
  <h2 class="abs section-title" style="top:988px">Latest <span>Properties</span></h2>

  <div class="abs feature-card"></div>
  <div class="abs photo feature-photo" role="img" aria-label="Photo of a white two-storey house with a garage and a tree"></div>
  <p class="abs feature-addr">4120 WILLOWMERE BEND LANE PALM SHORE,</p>
  <div class="abs pill" style="left:263px;top:1341px;width:121px">FL 33400</div>
  <div class="abs pill" style="left:388px;top:1341px;width:151px">$310,000</div>

  <p class="abs feature-lead"><b>/</b> LIST FOR 1.5% COMMISSION,</p>
  <p class="abs feature-sub">AND RECEIVE TOP MARKETING FROM REAL ESTATE PRO!</p>
  <div class="abs arrow-btn" style="left:620px;top:1331px"><svg width="12" height="14" viewBox="0 0 12 14"><path d="M10 1 L2 7 L10 13 Z" fill="none" stroke="#0255a3" stroke-width="1.6"/></svg></div>
  <div class="abs arrow-btn off" style="left:669px;top:1331px"><svg width="12" height="14" viewBox="0 0 12 14"><path d="M2 1 L10 7 L2 13 Z" fill="none" stroke="#ccc" stroke-width="1.6"/></svg></div>
</section>

<section>
  <div class="abs bracket l" style="left:162px;top:1520px;width:135px"></div>
  <div class="abs bracket r" style="left:893px;top:1520px;width:145px"></div>
  <h2 class="abs section-title" style="top:1500px">30 Day Listing Service <span>Guaranteed.</span></h2>

  <article class="abs listing" style="left:182px">
    <div class="photo" role="img" aria-label="Photo of a white two-storey house with a double garage"></div>
    <p class="addr">218 s Harbor Reach drive Seacliff, FL33470</p>
    <p class="price">$550,000</p>
    <ul><li>Professional Real Estate Photography</li><li>Comparative Market Analysis (CMA)</li><li>FREE Consultation with Real Estate Professional</li></ul>
    <div class="call">CALL US</div><div class="tel">555 - 318 - 6402</div>
  </article>
  <article class="abs listing" style="left:462px">
    <div class="photo" role="img" aria-label="Photo of a bright living room with a sofa, TV and ceiling fan" style="background:linear-gradient(180deg,#dcdcdc,#b9b9b9 60%,#8d8d8d)"></div>
    <p class="addr">218 s Harbor Reach drive Seacliff, FL33470</p>
    <p class="price">$550,000</p>
    <ul><li>Professional Real Estate Photography</li><li>Comparative Market Analysis (CMA)</li><li>FREE Consultation with Real Estate Professional</li></ul>
    <div class="call">CALL US</div><div class="tel">555 - 318 - 6402</div>
  </article>
  <article class="abs listing" style="left:741px">
    <div class="photo" role="img" aria-label="Photo of a cream two-storey house with palm trees" style="background:linear-gradient(170deg,#a9cdea 0%,#e6dcb8 45%,#d9cc9a 70%,#6f8b4c 100%)"></div>
    <p class="addr">218 s Harbor Reach drive Seacliff, FL33470</p>
    <p class="price">$550,000</p>
    <ul><li>Professional Real Estate Photography</li><li>Comparative Market Analysis (CMA)</li><li>FREE Consultation with Real Estate Professional</li></ul>
    <div class="call">CALL US</div><div class="tel">555 - 318 - 6402</div>
  </article>
</section>

<section>
  <div class="abs band" role="img" aria-label="Faint city skyline backdrop"></div>
  <h2 class="abs band-title">NOEL DARVEN, Lic. Real Estate Broker</h2>
  <p class="abs band-copy">On average, our customers save $5,600 when they list with us... and<br>they still receive top marketing and quality professional service!</p>
  <div class="abs band-btn">CONTACT CALMRIDGE AND SAVE TODAY!</div>
</section>

<footer>
  <p class="abs foot-note"><b>30 Day</b> Listing Service <b>GUARANTEED.</b> Save thousands $$$ listing with us!<br>Morbi eu sem felis. Integer faucibus ligula vitae enim vestibulum iaculis.</p>
  <div class="abs copyright">Copyright © 2018 Calmridge. All Rights Reserved.</div>
</footer>

</body>
</html>
```